Handmade candle business in melbourne requiring assistance with designing classy labels

My business name is Wick and Willow.
I specialise in making handmade candles, i'm based in Melbourne.
My moto is "Delicately hand poured and infused by me...for you"
wickwillow@mailbox-demo.net
0487 913 072

I need some assistance with designing my labels for my glass candles
I really like earthy colours and nothing too bright, but I want it to look classy and elegant and something that stands out from other homemade candle businesses.
I have attached a sample of a design that appeals to me but open to suggestions.

```html
<!DOCTYPE html>
<html lang="en">
<head>
<meta charset="utf-8">
<title>Wick and Willow – Candle Labels</title>
<link href="https://fonts.googleapis.com/css2?family=Quicksand:wght@500;600&family=Didact+Gothic&family=Allura&display=swap" rel="stylesheet">
<style>
  :root {
    --bark: #6b5045;
    --ink: #4a3a36;
    --white: #ffffff;
    --orange: #f8a84f;
    --orange-deep: #e8913a;
    --pink: #f5aab0;
    --pink-deep: #e8939b;
    --mint: #9ed3ad;
    --mint-deep: #86c398;
    --ring-mint: #8fd0b5;
    --ring-blue: #4fb6cf;
    --ring-pink: #f1a6ae;
  }
  * { box-sizing: border-box; margin: 0; padding: 0; }
  html, body {
    width: 1175px; height: 1200px; overflow: hidden; background: var(--white);
  }
  .sheet { position: relative; width: 1175px; height: 1200px; }

  .label {
    position: absolute;
    width: 952px; height: 330px;
    background: var(--bark);
    overflow: hidden;
  }
  .label--orange { left: 109px; top: 83px;  --petal: var(--orange); --petal-deep: var(--orange-deep); --ring: var(--ring-mint); --side: var(--ring-mint); }
  .label--pink   { left: 110px; top: 442px; --petal: var(--pink);   --petal-deep: var(--pink-deep);   --ring: var(--ring-blue); --side: var(--ring-blue); }
  .label--mint   { left: 114px; top: 807px; --petal: var(--mint);   --petal-deep: var(--mint-deep);   --ring: var(--ring-pink); --side: var(--ring-pink); }

  .bloom { position: absolute; inset: 0; width: 100%; height: 100%; }

  .side-credit {
    position: absolute;
    writing-mode: vertical-rl;
    white-space: nowrap;
    line-height: 1;
  }
  .side-credit__name {
    left: 52px; top: 112px;
    font-family: "Quicksand", sans-serif; font-weight: 500;
    font-size: 15px; color: var(--side);
  }
  .side-credit__maker {
    left: 36px; top: 185px;
    font-family: "Allura", cursive; font-size: 13px; color: var(--white);
  }
  .side-credit__email {
    left: 22px; top: 112px;
    font-family: "Didact Gothic", sans-serif;
    font-size: 9px; color: var(--orange); letter-spacing: 0.2px;
  }

  .badge {
    position: absolute;
    left: 332px; top: 31px;
    width: 280px; height: 280px;
    display: flex; flex-direction: column; align-items: center; justify-content: center;
    text-align: center;
  }
  .badge svg { position: absolute; inset: 0; }
  .badge__title {
    position: relative;
    font-family: "Quicksand", sans-serif; font-weight: 600;
    font-size: 26px; color: var(--ink); letter-spacing: 0.2px;
    margin-top: 8px;
  }
  .badge__maker {
    position: relative;
    font-family: "Allura", cursive; font-size: 22px; color: var(--white);
    align-self: flex-end; margin-right: 40px; margin-top: -8px;
  }
  .badge__motto {
    position: relative;
    font-family: "Didact Gothic", sans-serif; font-size: 13px; line-height: 1.25;
    color: var(--ink); margin-top: 6px;
  }
</style>
</head>
<body>
<main class="sheet">

  <section class="label label--orange">
    <svg class="bloom" viewBox="0 0 952 330" role="img" aria-label="Large hand-drawn dahlia illustration in orange petals outlined in brown">
      <defs>
        <radialGradient id="bloomOrange" cx="50%" cy="50%" r="55%">
          <stop offset="0" stop-color="var(--petal)"/>
          <stop offset="1" stop-color="var(--petal-deep)"/>
        </radialGradient>
      </defs>
      <ellipse cx="470" cy="175" rx="405" ry="250" fill="url(#bloomOrange)"/>
    </svg>
    <p class="side-credit side-credit__name">Wick and Willow</p>
    <p class="side-credit side-credit__maker">by Tess Halloran</p>
    <p class="side-credit side-credit__email">wickwillow@mailbox-demo.net</p>
    <div class="badge">
      <svg viewBox="0 0 280 280" aria-hidden="true">
        <circle cx="140" cy="140" r="140" fill="var(--ink)" fill-opacity="0.35"/>
        <circle cx="140" cy="140" r="126" fill="var(--petal)"/>
        <circle cx="140" cy="140" r="126" fill="#fff" fill-opacity="0.12"/>
        <circle cx="140" cy="140" r="126" fill="none" stroke="var(--ring)" stroke-width="4"/>
      </svg>
      <h2 class="badge__title">Wick and Willow</h2>
      <p class="badge__maker">by Tess Halloran</p>
      <p class="badge__motto">delicately hand poured<br>and infused by me…<br>for you</p>
    </div>
  </section>

  <section class="label label--pink">
    <svg class="bloom" viewBox="0 0 952 330" role="img" aria-label="Large hand-drawn dahlia illustration in pink petals outlined in brown">
      <defs>
        <radialGradient id="bloomPink" cx="50%" cy="50%" r="55%">
          <stop offset="0" stop-color="var(--petal)"/>
          <stop offset="1" stop-color="var(--petal-deep)"/>
        </radialGradient>
      </defs>
      <ellipse cx="470" cy="175" rx="405" ry="250" fill="url(#bloomPink)"/>
    </svg>
    <p class="side-credit side-credit__name">Wick and Willow</p>
    <p class="side-credit side-credit__maker">by Tess Halloran</p>
    <p class="side-credit side-credit__email">wickwillow@mailbox-demo.net</p>
    <div class="badge">
      <svg viewBox="0 0 280 280" aria-hidden="true">
        <circle cx="140" cy="140" r="140" fill="var(--ink)" fill-opacity="0.35"/>
        <circle cx="140" cy="140" r="126" fill="var(--petal)"/>
        <circle cx="140" cy="140" r="126" fill="#fff" fill-opacity="0.12"/>
        <circle cx="140" cy="140" r="126" fill="none" stroke="var(--ring)" stroke-width="4"/>
      </svg>
      <h2 class="badge__title">Wick and Willow</h2>
      <p class="badge__maker">by Tess Halloran</p>
      <p class="badge__motto">delicately hand poured<br>and infused by me…<br>for you</p>
    </div>
  </section>

  <section class="label label--mint">
    <svg class="bloom" viewBox="0 0 952 330" role="img" aria-label="Large hand-drawn dahlia illustration in mint green petals outlined in brown">
      <defs>
        <radialGradient id="bloomMint" cx="50%" cy="50%" r="55%">
          <stop offset="0" stop-color="var(--petal)"/>
          <stop offset="1" stop-color="var(--petal-deep)"/>
        </radialGradient>
      </defs>
      <ellipse cx="470" cy="175" rx="405" ry="250" fill="url(#bloomMint)"/>
    </svg>
    <p class="side-credit side-credit__name">Wick and Willow</p>
    <p class="side-credit side-credit__maker">by Tess Halloran</p>
    <p class="side-credit side-credit__email">wickwillow@mailbox-demo.net</p>
    <div class="badge">
      <svg viewBox="0 0 280 280" aria-hidden="true">
        <circle cx="140" cy="140" r="140" fill="var(--ink)" fill-opacity="0.35"/>
        <circle cx="140" cy="140" r="126" fill="var(--petal)"/>
        <circle cx="140" cy="140" r="126" fill="#fff" fill-opacity="0.12"/>
        <circle cx="140" cy="140" r="126" fill="none" stroke="var(--ring)" stroke-width="4"/>
      </svg>
      <h2 class="badge__title">Wick and Willow</h2>
      <p class="badge__maker">by Tess Halloran</p>
      <p class="badge__motto">delicately hand poured<br>and infused by me…<br>for you</p>
    </div>
  </section>

</main>
</body>
</html>
```